Post Lockdown Ortho Special

We are running a special for (Ortho) Braces/Clear Aligner (Quorventa), till July 31st 2020. Up to $2,000 off with free Consultation and Xrays.

We need a ad to run in different formats.

Maybe something with: what better time to get braces when you have to wear a mask all the time.

Trying to rebuild our business and get people in for free consultations.

```html
<!DOCTYPE html>
<html lang="en">
<head>
<meta charset="utf-8">
<title>Pinecrest Family Dentistry – Ortho Special</title>
<link href="https://fonts.googleapis.com/css2?family=Poppins:wght@400;500;600;700&family=Oswald:wght@500&family=Cormorant+SC:wght@600&display=swap" rel="stylesheet">
<style>
  :root{
    --purple:#6a4199;
    --purple-deep:#5a3486;
    --pink:#f5c9d8;
    --ink:#1f1a26;
    --lavender:#e4d8f0;
    --stage:#d8d8da;
    --white:#ffffff;
  }
  *{margin:0;padding:0;box-sizing:border-box}
  html,body{width:1200px;height:838px;overflow:hidden}
  body{background:var(--stage);font-family:"Poppins",sans-serif;position:relative}
  .banner{
    position:absolute;left:0;top:82px;width:1200px;height:675px;overflow:hidden;
    background:linear-gradient(100deg,var(--white) 0%,var(--white) 42%,#f1ebf7 62%,var(--lavender) 100%);
  }
  .photo{
    position:absolute;left:740px;top:0;width:460px;height:616px;
    background:
      radial-gradient(ellipse 42% 50% at 72% 42%,#e8b899 0%,#c89474 45%,rgba(150,100,70,0) 75%),
      linear-gradient(180deg,#d9cbe6 0%,#b28a6c 55%,#6a4a36 100%);
    opacity:.92;
  }
  .brand{position:absolute;left:23px;top:24px;display:flex;align-items:center;gap:20px}
  .brand-mark{width:96px;height:96px;border-radius:50%;background:var(--purple)}
  .brand-name{color:var(--purple);font-family:"Cormorant SC",serif;font-weight:600;line-height:1}
  .brand-name .main{display:block;font-size:36px;letter-spacing:1px}
  .brand-name .sub{display:block;font-size:14px;letter-spacing:6px;margin-top:4px}
  .brand-doctor{display:block;margin-top:8px;padding-top:6px;border-top:1px solid #9a86b3;
    font-family:"Cormorant SC",serif;font-size:13px;letter-spacing:1.5px;color:#6d6478;text-align:center}
  .headline{position:absolute;left:23px;top:142px;color:var(--purple);line-height:1}
  .headline .lead{display:block;font-size:41px;font-weight:400;letter-spacing:-.3px}
  .headline .punch{display:block;font-size:55px;font-weight:700;letter-spacing:-1px;margin-top:12px;line-height:1.18}
  .tag{position:absolute;left:23px;top:322px;height:48px;width:280px;color:var(--white);
    font-size:35px;font-weight:500;line-height:48px;padding-left:5px}
  .tag::before{content:"";position:absolute;inset:0;left:0;background:var(--pink);transform:translate(6px,4px) skewX(-18deg);transform-origin:bottom left;z-index:-1}
  .tag::after{content:"";position:absolute;inset:0;background:var(--purple);transform:skewX(-18deg);transform-origin:bottom left;z-index:-1}
  .tag{z-index:1}
  .treatments{position:absolute;left:23px;top:386px;display:flex;gap:26px;align-items:center}
  .treatment{display:flex;align-items:center;gap:8px;font-size:24px;color:var(--ink)}
  .treatment svg{width:48px;height:48px}
  .deadline{position:absolute;left:23px;top:448px;width:420px;height:37px;color:var(--white);
    font-size:22px;letter-spacing:8px;line-height:37px;padding-left:6px;z-index:1}
  .deadline::after{content:"";position:absolute;inset:0;background:var(--purple);transform:skewX(-22deg);transform-origin:bottom left;z-index:-1}
  .deadline b{font-weight:700}
  .offer{position:absolute;left:23px;top:500px;width:352px;height:108px;border-radius:6px;background:var(--purple);color:var(--white)}
  .offer .upto{position:absolute;left:10px;top:10px;width:21px;height:88px;background:var(--white);color:var(--purple);
    writing-mode:vertical-rl;transform:rotate(180deg);font-size:13px;letter-spacing:5px;text-align:center;line-height:21px}
  .offer .amount{position:absolute;left:36px;top:-8px;font-family:"Oswald",sans-serif;font-weight:500;font-size:100px;letter-spacing:-2px;line-height:1.2}
  .offer .off{position:absolute;right:12px;top:10px;font-family:"Oswald",sans-serif;font-weight:500;font-size:30px}
  .perks{position:absolute;left:390px;top:522px;padding-left:8px;border-left:1.5px solid var(--purple-deep);
    font-size:22px;line-height:28px;color:var(--ink)}
  .contact{position:absolute;left:0;top:616px;width:1200px;height:59px;background:var(--purple);color:var(--white);
    display:flex;align-items:center;font-size:24px}
  .contact-item{position:absolute;display:flex;align-items:center;gap:5px;top:12px}
  .contact-item svg{width:34px;height:34px}
</style>
</head>
<body>
  <main class="banner">
    <div class="photo" role="img" aria-label="Photo of a smiling teenage girl with braces in front of a woman wearing a face mask"></div>

    <div class="brand">
      <span class="brand-mark"></span>
      <div>
        <span class="brand-name"><span class="main">PINECREST</span><span class="sub">FAMILY DENTISTRY</span></span>
        <span class="brand-doctor">Dr Maren Holloway</span>
      </div>
    </div>

    <h1 class="headline">
      <span class="lead">What better time to get braces</span>
      <span class="punch">when you have to wear a<br>mask all the time.</span>
    </h1>

    <div class="tag">SPECIAL FOR</div>

    <ul class="treatments" style="list-style:none">
      <li class="treatment">
        <svg viewBox="0 0 48 48" aria-hidden="true"><circle cx="24" cy="24" r="22.5" fill="none" stroke="#6a4199" stroke-width="2"/><rect x="8" y="19" width="32" height="10" rx="4" fill="none" stroke="#6a4199" stroke-width="2"/><line x1="16" y1="19" x2="16" y2="29" stroke="#6a4199" stroke-width="2"/><line x1="24" y1="19" x2="24" y2="29" stroke="#6a4199" stroke-width="2"/><line x1="32" y1="19" x2="32" y2="29" stroke="#6a4199" stroke-width="2"/></svg>
        Braces (Ortho)
      </li>
      <li class="treatment">
        <svg viewBox="0 0 48 48" aria-hidden="true"><circle cx="24" cy="24" r="22.5" fill="none" stroke="#6a4199" stroke-width="2"/><path d="M12 14 C12 32 18 38 24 38 C30 38 36 32 36 14 L31 14 C31 27 28 31 24 31 C20 31 17 27 17 14 Z" fill="#6a4199"/></svg>
        Clear Aligner (Quorventa)
      </li>
    </ul>

    <div class="deadline">till July <b>31st 2020</b></div>

    <div class="offer">
      <span class="upto">UPTO</span>
      <span class="amount">$2,000</span>
      <span class="off">OFF</span>
    </div>

    <p class="perks">with free Consultation<br>and Xrays.</p>

    <footer class="contact">
      <span class="contact-item" style="left:23px">
        <svg viewBox="0 0 34 34" aria-hidden="true"><circle cx="17" cy="17" r="15.5" fill="none" stroke="#fff" stroke-width="2"/><path d="M11 9 l4 0 l1.5 4.5 l-2.3 1.6 c1 2.3 2.6 3.9 4.8 4.8 l1.6-2.3 l4.4 1.5 l0 4 c-8 .8-14.8-6-14-14z" fill="#fff"/></svg>
        +1 555-210-4477
      </span>
      <span class="contact-item" style="left:284px">
        <svg viewBox="0 0 34 34" aria-hidden="true"><circle cx="17" cy="17" r="15.5" fill="none" stroke="#fff" stroke-width="2"/><rect x="9" y="11" width="16" height="12" rx="2" fill="#fff"/><path d="M9.5 12 L17 18 L24.5 12" fill="none" stroke="#6a4199" stroke-width="1.6"/></svg>
        marenhollowaydds@pinemail.com
      </span>
      <span class="contact-item" style="left:783px">
        <svg viewBox="0 0 34 34" aria-hidden="true"><circle cx="17" cy="17" r="15.5" fill="none" stroke="#fff" stroke-width="2"/><circle cx="17" cy="17" r="8" fill="none" stroke="#fff" stroke-width="1.5"/><ellipse cx="17" cy="17" rx="3.5" ry="8" fill="none" stroke="#fff" stroke-width="1.5"/><line x1="9" y1="17" x2="25" y2="17" stroke="#fff" stroke-width="1.5"/></svg>
        www.dentistinpinecrest.com
      </span>
    </footer>
  </main>
</body>
</html>
```